Flyer für Anbieter von handgemachtem Schmuck
Zielgruppe
Ich mache handgemachten Schmuck aus Feinsilber (siehe Kramly Link). Im Speziellen verewige ich Nasen-oder Pfotenabdruck von Haustieren in Feinsilber. Dazu habe ich eine Zusammenarbeit mit dem Kleintierkrematorium Wolfsmatt (https://laden51830264.shopvelo.example/Silber-Anh%C3%A4nger-mit-Pfoten-oder-Nasenabdruck-Ihres-geliebten-Haustiers-p417285063). Nun möchte ich das Angebot ausbauen und bei Tierärzten oder Hundesalons bekannt machen. Dabei soll kein klassisches „Trauerprodukt“ kommuniziert werden, sondern eine hochwertige, persönliche Erinnerung, die zu Lebzeiten wie auch später eine Bedeutung haben kann („dein Tier immer nah bei dir“). Dazu brauche ich einen Flyer (mit 1 Falz?). Der Flyer soll dieses spezielle Angebot erklären und bewerben.
Auf der Vorderseite fände ich ein emotionales Bild von Hund und Katze schön. Und auch ein Bild von meinem Schmuck sollte zu sehen sein (Bild kann ich ggf. liefern).
Im weiteren Verlauf sehe ich eine Erklärung, wie alles funktioniert (so wie es beim Produkt auf Kramly steht). Mein Logo, Kontaktdaten sowie der Link zu Kramly (QR Code) sollen ebenfalls enthalten sein.
Der Abdruck kann sowohl als Anhänger für eine Halskette, aber auch (dann ohne Öse) als Medaillon zum Aufbewahren gefertigt werden. Auch gut als Geschenkidee geeignet.
Der Anhänger kostet rund Fr. 200, also kein günstiger Modeschmuck. Aber auch kein Andenken aus Asche, das rund 1000-5000.- kostet.
Zielgruppe: Haustierhalter ab mittleren Alters mit Affinität zu Silberschmuck. Schenkende.
Den Flyer möchte ich in Tierarztpraxen und Hundesalons verteilen. Aber auch neben meinem sonstigen Schmuck im stationären Handel und Marktständen hinlegen.
Aufgabenstellung
Wenn möglich meine Farben (Mintgrün/dunkelgrün/weiss/schwarz) übernehmen. Das Logo ( Pfau mit Roswitha Feinschmuck) soll ebenfalls gut zu sehen sein.

```html
<!DOCTYPE html>
<html lang="de">
<head>
<meta charset="utf-8">
<title>Flyer – Roswitha Feinschmuck</title>
<link href="https://fonts.googleapis.com/css2?family=Alex+Brush&family=Josefin+Sans:wght@300;400&display=swap" rel="stylesheet">
<style>
  :root {
    --stage: #ececec;
    --paper: #ffffff;
    --mint: #cfe7d9;
    --mint-light: #dcefe4;
    --mint-band: #bfe0cc;
    --ink: #1c1c1c;
    --ink-soft: #333333;
    --silver-light: #f2f2f2;
    --silver-dark: #9c9c9c;
    --sketch-dark: #8e8e8e;
    --sketch-light: #ededed;
  }
  * { box-sizing: border-box; margin: 0; padding: 0; }
  html, body { width: 1200px; height: 1200px; overflow: hidden; }
  body {
    background: var(--stage);
    font-family: "Josefin Sans", sans-serif;
    color: var(--ink);
    display: flex;
    justify-content: center;
    align-items: center;
    gap: 40px;
  }
  .panel {
    width: 500px;
    height: 1070px;
    box-shadow: 0 4px 14px rgba(0,0,0,0.12);
    position: relative;
    overflow: hidden;
  }

  /* Info side */
  .panel--info {
    background: var(--paper);
    padding: 46px 40px 30px;
    text-align: center;
    font-weight: 300;
    font-size: 14.5px;
    line-height: 1.42;
    color: var(--ink-soft);
    display: flex;
    flex-direction: column;
  }
  .script-heading {
    font-family: "Alex Brush", cursive;
    font-weight: 400;
    color: var(--ink);
    background: linear-gradient(90deg, transparent 0%, var(--mint-band) 8%, var(--mint-band) 92%, transparent 100%);
    display: inline-block;
    align-self: center;
    padding: 2px 22px 0;
    line-height: 1.2;
  }
  .script-heading--main { font-size: 22px; margin-bottom: 14px; padding: 4px 18px 2px; }
  .script-heading--main span { display: block; white-space: nowrap; }
  .script-heading--section { font-size: 25px; margin: 14px 0 12px; }
  .info-text { margin-bottom: 12px; }
  .contact {
    margin-top: auto;
    align-self: center;
    background: linear-gradient(90deg, transparent 0%, var(--mint-band) 6%, var(--mint-band) 94%, transparent 100%);
    padding: 10px 26px;
    text-align: left;
    font-size: 12px;
  }
  .contact-row { display: flex; align-items: center; gap: 12px; padding: 3px 0; }
  .contact-icon { width: 20px; height: 20px; flex: none; }

  /* Cover side */
  .panel--cover {
    background: linear-gradient(180deg, var(--mint) 0%, var(--mint-light) 100%);
    display: flex;
    flex-direction: column;
    align-items: center;
  }
  .brand {
    margin-top: 150px;
    display: flex;
    align-items: center;
    gap: 12px;
  }
  .brand-dot { width: 12px; height: 12px; border-radius: 50%; background: var(--ink); }
  .brand-name {
    font-family: "Josefin Sans", sans-serif;
    font-weight: 400;
    font-size: 28px;
    line-height: 1;
    color: var(--ink);
    white-space: nowrap;
  }
  .pendant {
    margin-top: 80px;
    width: 140px;
    height: 140px;
    border-radius: 50%;
    background: radial-gradient(circle at 40% 35%, var(--silver-light) 0%, #d4d4d4 55%, var(--silver-dark) 100%);
  }
  .cover-title {
    font-family: "Alex Brush", cursive;
    font-weight: 400;
    font-size: 52px;
    margin-top: 56px;
    line-height: 1;
  }
  .cover-subtitle {
    margin-top: 14px;
    font-weight: 300;
    font-size: 17px;
    line-height: 1.35;
    text-align: center;
  }
  .cover-illustration {
    position: absolute;
    left: 0; right: 0; bottom: 0;
    height: 410px;
    background: linear-gradient(160deg, var(--sketch-dark) 0%, #bdbdbd 35%, var(--sketch-light) 70%, #ffffff 100%);
  }
</style>
</head>
<body>

  <section class="panel panel--info">
    <h2 class="script-heading script-heading--main"><span>Silber-Anhänger mit Pfoten- oder Nasenabdruck</span><span>Ihres geliebten Haustiers oder mit Fingerabdruck</span></h2>
    <p class="info-text">Manche Spuren kann man für immer festhalten. Der Abdruck einer Pfote. Die feine Struktur einer Nase.</p>

    <h3 class="script-heading script-heading--section">Der Ablauf – ein echtes 1:1 Unikat</h3>
    <p class="info-text">Aus dem originalen Abdruck Ihres Haustiers entsteht ein einzigartiges Schmuckstück – so individuell wie die Erinnerung selbst.</p>
    <p class="info-text">Der Abdruck wird behutsam direkt im Krematorium mit Silikon genommen.</p>
    <p class="info-text">Bei Katzen eignet sich besonders der Nasenabdruck. Bei Hunden kommt meist die Pfotenstruktur wundervoll zur Geltung – auf Wunsch auch ein Teil der Nase. Bei ganz kleinen Tieren kann die ganze Pfote abgeformt werden.</p>

    <h3 class="script-heading script-heading--section">Handgemacht mit Herz</h3>
    <p class="info-text">In respektvoller und sorgfältiger Handarbeit wird der Originalabdruck anschliessend in einem Atelier in der Region Basel in einen edlen Anhänger aus Feinsilber verwandelt. Ihr persönliches Andenken wird mit der Verantwortlichkeitsmarke des Ateliers versehen.</p>

    <h3 class="script-heading script-heading--section">Verewigt in Feinsilber</h3>
    <p class="info-text">Der einzigartige Silberschmuck bewahrt die Verbindung sichtbar und spürbar – nah am Herzen. Sie erhalten Ihr persönliches Unikat in einer hochwertigen Verpackung – auch als besonderes Geschenk für einen trauernden Menschen.</p>
    <p class="info-text">Ob als Anhänger an einer Halskette oder als Medaillon zum behutsamen Aufbewahren – ein Zeichen der Verbundenheit, das bleiben darf. Der Anhänger wird ohne Öse zum stillen Andenken. Ein Zeichen der Liebe.</p>

    <div class="contact">
      <div class="contact-row">
        <svg class="contact-icon" viewBox="0 0 24 24" fill="none" stroke="#1c1c1c" stroke-width="1.5" aria-hidden="true">
          <path d="M2 4h3l2.5 11h11l2-8H6.5"/>
          <circle cx="9" cy="19" r="1.5"/><circle cx="17" cy="19" r="1.5"/>
        </svg>
        <span>roswitha-feinschmuck.kramly.com</span>
      </div>
      <div class="contact-row">
        <svg class="contact-icon" viewBox="0 0 24 24" fill="none" stroke="#1c1c1c" stroke-width="1.5" aria-hidden="true">
          <circle cx="12" cy="12" r="10.5"/>
          <rect x="6.5" y="8.5" width="11" height="7.5"/>
          <path d="M6.5 8.5l5.5 4.5 5.5-4.5"/>
        </svg>
        <span>hallo@roswitha-feinschmuck.ch</span>
      </div>
    </div>
  </section>

  <section class="panel panel--cover">
    <div class="brand">
      <span class="brand-dot"></span>
      <p class="brand-name">Roswitha Feinschmuck</p>
    </div>
    <div class="pendant" role="img" aria-label="Foto eines runden Feinsilber-Anhängers mit Pfotenabdruck und Öse"></div>
    <h1 class="cover-title">Silber-Anhänger</h1>
    <p class="cover-subtitle">mit Pfoten- oder Nasenabdruck<br>Ihres geliebten Haustiers oder<br>mit Fingerabdruck</p>
    <div class="cover-illustration" role="img" aria-label="Bleistiftzeichnung einer Frau mit langem Haar, die zärtlich ihren Hund umarmt"></div>
  </section>

</body>
</html>
```